Verpackungsdesign für italienische Produkte gesucht
Die Zusammenarbeit mit dem Designer 7Pixo hat sehr viel Spaß gemacht. Jeder Änderungswunsch wurde super schnell in die Tat umgesetzt. Die Kommunikation verlief reibungslos. Das Ergebnis ist einfach klasse geworden. Er hat ein großes Talent für den Entwurf von Designs. Ich freue mich sehr darauf, auch zukünftige Projekte mit ihm durchführen zu können. Vielen Dank nochmal an Ihn für die tolle Arbeit und die Unterstützung. Ich kann eine Zusammenabeit mit dem Designer 7Pixo nur empfehlen.
Liebe Designerinnen und Designer,
wir sind ein Unternehmen, welches Olivenöl, Pasta und Wein sowie Olivenblättertee und Tomatensoße auf Sizilien (Italien) in Gibellina produziert. In vierter Generation produziert die Familie Berardi landwirtschaftliche Erzeugnisse, die nach biologischen Prinzipien angebaut werden. Im Ackerbau verzichten wir auf synthetisch hergestellte Pflanzenschutzmittel, Mineraldünger und Grüne Gentechnik. Da in der heutigen Zeit viele Konsumenten den Ursprung der gekauften Produkte nicht mehr zurückverfolgen können und ihnen in dieser Hinsicht kaum Transparenz gewährleistet wird, möchten wir im Namen der Familie Berardi unseren Kunden den Herstellungsprozess vom Anbau bis zur Fertigstellung des Enderzeugnisses transparent aufzeigen und sie für die bewusste und gesunde Ernährung sensibilisieren.
Unsere Zielgruppe sind ernährungsbewusste Personen, überwiegend Frauen im mittleren Alter, die auf bewusste, gesunde Ernährung viel Wert legen.
Vielen lieben Dank für eure Arbeit im Voraus. Ich freue mich sehr auf die Designvorschläge.
Lieben Gruß
Marta & Lorenzo Berardi
KREATIVE DESIGNER gesucht
WIR SUCHEN EIN VERPACKUNGSKONZEPT FÜR UNSERE PRODUKTE
Für unsere Produkte: Olivenöl, Pasta und Wein sowie Olivenblättertee und Tomatensoße benötigen wir ein Verpackungsdesign, welches erkennen lässt, dass die Produkte zu einer Produktfamilie gehören. Darüber hinaus benötigen wir das Design für den Kartonanhänger, der an jedes unserer Produkte ran gehängt werden soll.
Erst einmal suchen wir nach Vorschlägen für ein Verpackungsdesign. Im Anschluss an dieses Projekt würden wir gerne mit dem Designer die Reinzeichnungen fertig erstellen. Den Preis für die Reinzeichnung würden wir dann gerne mit dem Designer verhandeln.
Mit dem Designer, der das Projekt gewinnt, streben wir auch nach dem Produktende eine enge Zusammenarbeit an, da sich unser Produktportfolio stetig erweitern wird und Folgeaufträge bereits in Planung sind.
Für die Produkte Olivenöl, Pasta und Tee sowie Tomatensoße benötigen wir Etiketten mit Vorder- und Rückseite. Für die Pasta-Verpackung soll ein Design für den Kartonreiter aus dünnem Kartonpapier erstellt werden (siehe Bild Pasta Design Beispiel). Dieses Kartonpapier könnte schwarz sein, da die Olivenölflasche, die Weinflaschen sowie die Verpackung für Tee und die Flasche für Tomatensoße ebenfalls dunkel sind.
Das Design sollte elegant und qualitativ hochwertig aussehen. Mit unseren Produkten sollen die folgenden Werte transportiert werden: Tradition, Familie, hochwertige Qualität, Transparenz, biologischer Anbau, bewusste Ernährung, Liebe zum Produkt, Sizilien,
Es sollten max. 4 verschiedene Farben verwendet werden.
In der Datei Vorgaben zum Design stehen weitere Angaben. Zusätzlich besteht eine PDF Datei mit Bildern zur Gestaltungshilfe. Eine weitere Datei besteht mit allen Verpackungen, die gestaltet werden sollen.
Alle Logos sind auch noch in weiteren Formaten verfügbar.
Vielen Dank im Voraus
Marta & ..

```html
<!DOCTYPE html>
<html lang="de">
<head>
<meta charset="utf-8">
<title>Berardi – Fussili Kartonreiter</title>
<link rel="stylesheet" href="https://fonts.googleapis.com/css2?family=Cinzel:wght@400&family=Yellowtail&family=Roboto+Condensed:wght@700&display=swap">
<style>
  :root {
    --page-bg: #ffffff;
    --slate-dark: #151516;
    --slate-mid: #2b2b2d;
    --slate-light: #3c3c3e;
    --sauce: #b0502a;
    --pasta: #d9a24c;
    --organic-green: #8dbb2d;
    --ink-light: #f4f1ea;
  }
  * { margin: 0; padding: 0; box-sizing: border-box; }
  html, body {
    width: 1200px;
    height: 1200px;
    overflow: hidden;
    background: var(--page-bg);
  }
  .header-card {
    position: absolute;
    left: 80px;
    top: 150px;
    width: 1040px;
    height: 900px;
    overflow: hidden;
    color: var(--ink-light);
  }
  .table-scene {
    position: absolute;
    inset: 0;
    background:
      radial-gradient(ellipse 46% 22% at 45% 4%, var(--sauce) 0%, #6a3321 35%, transparent 70%),
      radial-gradient(ellipse 60% 36% at 45% 6%, #232324 0%, #1b1b1c 70%, transparent 72%),
      linear-gradient(160deg, var(--slate-light) 0%, var(--slate-mid) 35%, var(--slate-dark) 100%);
  }
  .organic-badge {
    position: absolute;
    left: 800px;
    top: 45px;
    width: 183px;
    height: 122px;
    background: var(--organic-green);
  }
  .brand {
    position: absolute;
    left: 0;
    right: 0;
    top: 495px;
    display: flex;
    justify-content: center;
  }
  .brand-name {
    margin-left: 30px;
    width: 302px;
    padding: 6px 0 4px;
    border-top: 2px solid var(--ink-light);
    border-bottom: 2px solid var(--ink-light);
    font-family: "Cinzel", serif;
    font-size: 50px;
    line-height: 56px;
    letter-spacing: 1px;
    text-align: center;
    text-transform: uppercase;
  }
  .product-name {
    position: absolute;
    left: 0;
    right: 0;
    top: 610px;
    padding-left: 30px;
    text-align: center;
    font-family: "Yellowtail", cursive;
    font-size: 150px;
    line-height: 160px;
  }
  .cooking-time {
    position: absolute;
    left: 0;
    right: 0;
    top: 798px;
    padding-left: 30px;
    text-align: center;
    font-family: "Roboto Condensed", sans-serif;
    font-weight: 700;
    font-size: 25px;
    letter-spacing: 1px;
  }
</style>
</head>
<body>
  <section class="header-card">
    <div class="table-scene" role="img" aria-label="Dunkle Schieferplatte mit einem Teller Spaghetti mit Garnelen und Tomatensoße, geröstetem Knoblauch und alten Gabeln"></div>
    <div class="organic-badge" role="img" aria-label="Bio-Siegel"></div>
    <div class="brand">
      <div class="brand-name">Berardi</div>
    </div>
    <h1 class="product-name">Fussili</h1>
    <p class="cooking-time">Kochzeit ca. 6 Minuten</p>
  </section>
</body>
</html>
```